Stationery and Logo Design Project for new NZ Accounting Firm

Our company name is based in Auckland, New Zealand and is called DHW CA Limited. We are a chartered accountancy firm hence the CA abbreviations.

We need a full logo stationery design: Logo, Letterhead, Business Card and Compliments slip.

We are looking for a bold, modern and clean/simple design that makes us stand out. We want to stand out as professionals in the industry and would like the logo and stationery that our clients see to convey this image. We also want to break away from the traditional boring views of book/bean accountants. We are not doing the same old things others are doing and are mainly cloud based but with face to face business relationship focused as well.

We see ourselves as business advisers that provide more than just filing their tax returns. We want to add value to their business and be a partner in their business ventures.

We want the logo to convey the above and also attract potential clients when they see our ads among the thousands on vornix and the civic atlas.

The logo can be for the "DHW" with CA Ltd seperately or a logo/design beside the DHW. But open to other suggestions or concept.

Hi Designers

The designs I have received so far is not quite what I want.

I want something modern and bold that is DIFFERENT from others, from the usual logo designs. Some logo that when people look at it they will remember it as opposed to fading in the background of other competitors' logo.

Lower case lettering for the DHW could be something to explore as I have not seen a lot of these and they do appeal to me.

Thanks

We can focus on the logo first as that will form the main part for all stationery.

Reason: Final stages of choosing a logo design so need to time for designers to submit the letterhead, namecards designs.

Our target clients are small to medium business ranging from the sole trader to 50 employees businesses

Business

```html
<!DOCTYPE html>
<html lang="en">
<head>
<meta charset="utf-8">
<title>DHW CA Limited – Business Card</title>
<link href="https://fonts.googleapis.com/css2?family=Tinos:wght@400;700&display=swap" rel="stylesheet">
<style>
  :root {
    --backdrop: #8a8a8a;
    --card: #151515;
    --card-edge: #262626;
    --ink: #f2f2f2;
    --green: #8cc63f;
    --silver: #e9e9e9;
  }
  * { margin: 0; padding: 0; box-sizing: border-box; }
  html, body {
    width: 1067px; height: 1200px; overflow: hidden;
    background: var(--backdrop);
    font-family: "Tinos", "Times New Roman", serif;
  }
  .stage {
    position: relative; width: 1067px; height: 1200px;
    display: flex; flex-direction: column; align-items: center;
    justify-content: center; gap: 90px;
  }
  .card {
    position: relative; width: 760px; height: 434px;
    background: radial-gradient(ellipse at 50% 35%, var(--card-edge), var(--card) 70%);
    box-shadow: 0 18px 40px rgba(0,0,0,.45);
    overflow: hidden;
  }
  /* Front */
  .card--front {
    display: flex; flex-direction: column; align-items: center; justify-content: center;
  }
  .wordmark {
    font-weight: 700; color: var(--ink);
    font-size: 124px; line-height: 1; letter-spacing: 2px;
  }
  .firm-line {
    color: var(--ink); font-size: 29px; letter-spacing: 1px;
    margin-top: 2px; text-transform: uppercase; white-space: nowrap;
  }
  .web {
    color: var(--green); font-size: 22px; letter-spacing: 1px; margin-top: 46px;
  }
  /* Back */
  .edge-band {
    position: absolute; left: 0; top: 0; width: 78px; height: 100%;
    display: flex; flex-direction: column;
  }
  .edge-band__silver { flex: 0 0 44%; background: linear-gradient(90deg, #bdbdbd, var(--silver) 55%, #cfcfcf); }
  .edge-band__green { flex: 1; background: linear-gradient(90deg, #6fa82e, var(--green) 55%, #a6d65c); }
  .card--back .content { position: absolute; left: 128px; top: 56px; right: 40px; }
  .card--back .wordmark { font-size: 84px; }
  .card--back .firm-line { font-size: 19px; margin-top: 0; }
  .contact { margin-top: 56px; color: var(--ink); font-size: 17px; line-height: 1.55; white-space: nowrap; }
  .contact__name { color: var(--green); font-size: 27px; letter-spacing: 1px; }
  .contact__role { color: var(--ink); font-size: 16px; margin-left: 12px; letter-spacing: 0; }
  .contact__label { color: var(--green); }
  .contact__pair span + span { margin-left: 22px; }
  .contact .web { margin-top: 4px; font-size: 21px; text-align: left; }
</style>
</head>
<body>
<main class="stage">
  <section class="card card--front">
    <div class="wordmark">DHW</div>
    <div class="firm-line">Chartered Accountancy Ltd</div>
    <div class="web">www.DHWCALTD.com</div>
  </section>

  <section class="card card--back">
    <div class="edge-band">
      <div class="edge-band__silver"></div>
      <div class="edge-band__green"></div>
    </div>
    <div class="content">
      <div class="wordmark">DHW</div>
      <div class="firm-line">Chartered Accountancy Ltd</div>
      <div class="contact">
        <div class="contact__name">SAM CARTER<span class="contact__role">Manager</span></div>
        <div>18 Harbour View Road, Auckland 1010</div>
        <div class="contact__pair"><span><span class="contact__label">p:</span> + (09) 555 0142</span><span><span class="contact__label">m:</span> + (021) 555 0187</span></div>
        <div class="contact__pair"><span><span class="contact__label">f:</span> + (09) 555 0163</span><span><span class="contact__label">e:</span> sam.carter@dhwcaltd.com</span></div>
        <div class="web">www.DHWCALTD.com</div>
      </div>
    </div>
  </section>
</main>
</body>
</html>
```